BRASKET LAND SERVICES BILLBOARD DESIGN

I NEED A BILLBOARD FOR MY BUSINESS. WE ARE A LAND CLEARING COMPANY AND I WOULD LIKE TO ADD A PICTURE OF MY TRACK LOADER TO THE SIGN. OPEN TO COLORS. I WOULD ALSO LIKE TO HAVE MY PHONE NUMBER 555-284-6170, WEBSITE WWW.BRASKETLANDSERVICES.EXAMPLE, AND EMAIL ON THE SIGN (CONTACT@BRASKETLANDSERVICES.EXAMPLE). DESIGNERS CAN HAVE THE FREEDOM TO DO WHATEVER STYLE THEY WANT AND TO USE ANY COLORS THEY WANT.

Target Market(s)

ANYONE WITH PROPERTY

Requirements
Must have
• PICTURE OF TRACK LOADER, WEBSITE, PHONE NUMBER, EMAIL
Nice to have
• OPEN TO ANYTHING
Should not have
• OPEN TO ANYTHING

```html
<!DOCTYPE html>
<html lang="en">
<head>
<meta charset="utf-8">
<title>Brasket Land Services Billboard</title>
<link rel="stylesheet" href="https://fonts.googleapis.com/css2?family=Oswald:wght@600;700&family=Roboto:ital,wght@1,700;1,900&display=swap">
<style>
  :root {
    --stage: #5b5b5b;
    --paper: #ffffff;
    --orange: #e4522b;
    --ink: #1d1d1d;
    --photo-dark: #3a3b2c;
    --photo-green: #55603a;
    --photo-orange: #c9532d;
    --photo-soil: #8a7a55;
  }
  * { box-sizing: border-box; margin: 0; padding: 0; }
  html, body { width: 1069px; height: 1200px; overflow: hidden; background: var(--stage); }
  .billboard {
    position: absolute; left: 20px; top: 337px;
    width: 1029px; height: 525px;
    background: var(--paper);
    overflow: hidden;
    box-shadow: 0 6px 18px rgba(0,0,0,.35);
  }
  .hero-photo {
    position: absolute; left: 0; top: 0; width: 100%; height: 318px;
    background:
      radial-gradient(ellipse 30% 45% at 18% 55%, var(--photo-orange) 0%, transparent 70%),
      radial-gradient(ellipse 30% 45% at 85% 50%, var(--photo-orange) 0%, transparent 70%),
      linear-gradient(180deg, var(--photo-green) 0%, var(--photo-dark) 55%, var(--photo-soil) 100%);
  }
  .torn-edge { position: absolute; left: 0; top: 290px; width: 100%; height: 40px; }
  .brand-title {
    position: absolute; left: 300px; top: 20px; width: 340px;
    font-family: "Oswald", sans-serif; font-weight: 700;
    color: var(--paper); text-align: center;
    font-size: 88px; line-height: 88px;
    transform: skewX(-4deg);
    text-shadow: 4px 4px 0 #111, 6px 6px 8px rgba(0,0,0,.5);
  }
  .brand-title span { display: block; }
  .brand-title .line-wide { margin-left: 10px; }
  .hanger { position: absolute; left: 680px; top: 170px; width: 240px; height: 110px; }
  .call-card {
    position: absolute; left: 625px; top: 262px; width: 385px; height: 186px;
    background: var(--orange);
    transform: rotate(-8deg);
    font-family: "Oswald", sans-serif; font-weight: 600;
    color: var(--paper); text-align: center;
    padding-top: 22px;
  }
  .call-card .cta { font-size: 66px; line-height: 70px; letter-spacing: 1px; }
  .call-card .phone { font-size: 58px; line-height: 62px; letter-spacing: 1px; }
  .services {
    position: absolute; left: 32px; top: 322px;
    font-family: "Roboto", sans-serif; font-style: italic;
  }
  .services h2 { color: var(--orange); font-weight: 900; font-size: 60px; line-height: 68px; }
  .services ul { list-style: none; margin-top: 4px; }
  .services li {
    font-weight: 700; font-size: 22px; line-height: 29px; color: var(--ink);
    padding-left: 14px; position: relative;
  }
  .services li::before {
    content: ""; position: absolute; left: 0; top: 11px;
    width: 6px; height: 6px; border-radius: 50%; background: var(--orange);
  }
  .contact {
    position: absolute; right: 14px; top: 467px; text-align: left;
    font-family: "Roboto", sans-serif; font-style: italic; font-weight: 700;
    font-size: 15px; line-height: 19px;
  }
  .contact .email { color: var(--ink); }
  .contact .web { color: var(--orange); }
</style>
</head>
<body>
  <main class="billboard">
    <div class="hero-photo" role="img" aria-label="Photo of two orange tracked loaders with forestry mulcher heads parked among trees"></div>
    <svg class="torn-edge" viewBox="0 0 1029 40" preserveAspectRatio="none">
      <path d="M0 14 L40 10 L80 16 L130 9 L180 15 L240 11 L300 17 L360 10 L420 15 L480 9 L540 16 L600 11 L660 15 L720 8 L780 14 L840 10 L900 16 L960 11 L1029 14 L1029 40 L0 40 Z" fill="#ffffff"/>
    </svg>

    <h1 class="brand-title">
      <span>BRASKET</span>
      <span>LAND</span>
      <span class="line-wide">SERVICES</span>
    </h1>

    <svg class="hanger" viewBox="0 0 240 110">
      <polyline points="20,100 100,8 220,70" fill="none" stroke="#ffffff" stroke-width="5"/>
      <polyline points="20,100 100,8 220,70" fill="none" stroke="#e4522b" stroke-width="2"/>
      <circle cx="100" cy="8" r="6" fill="#e4522b" stroke="#ffffff" stroke-width="2"/>
    </svg>

    <div class="call-card">
      <div class="cta">CALL NOW!</div>
      <div class="phone">555-284-6170</div>
    </div>

    <section class="services">
      <h2>SERVICES</h2>
      <ul>
        <li>Trails and Road Clearing</li>
        <li>Elimination of Invasive Plant Species</li>
        <li>Fence and Survey Line Clearing</li>
        <li>Fire Break Construction</li>
      </ul>
    </section>

    <div class="contact">
      <div class="email">CONTACT@BRASKETLANDSERVICES.EXAMPLE</div>
      <div class="web">WWW.BRASKETLANDSERVICES.EXAMPLE</div>
    </div>
  </main>
</body>
</html>
```